Web site for Tree Removal Company

What we are looking for:
-------------------------------
Looking for a wordpress web site, you can provide your own template or we can supply you with one (http://quorvel.plindatheme.net).

What we do
---------------
To see what we do please go to google Australia and google "Tree removal Sydney" or "Tree Removal Melbourne".

Web site requirements
-----------------------------
We prefer you to use our template as it has all our requirements in already.
- Responsive.
- Based on Wordpress.
- Full complaint and compatible with plugs.

Look, Feel and Appearance
------------------------------------
Please use the logo (see attached), for colour scheme, look and feel of the web site.

Thank you for your time and effort!

Target Market(s)

Tree Removal for Residential Homes

Industry/Entity Type

It Company

Number of Pages Required

4 page

Font styles to use
Serif
Sans Serif

Requirements
Must have
• Wordpress
Nice to have
• Original artwork, images and text
Should not have
• non related images or wording

```html
<!DOCTYPE html>
<html lang="en">
<head>
<meta charset="utf-8">
<title>Leafwell — Tree Removal</title>
<link href="https://fonts.googleapis.com/css2?family=PT+Sans:wght@400;700&family=Arimo:wght@400;700&family=Montserrat:wght@600;700&display=swap" rel="stylesheet">
<style>
:root{
  --black:#000;
  --dark:#232323;
  --green:#5fcf8e;
  --green-band:#7fd8a0;
  --green-deep:#3fae6f;
  --text:#333;
  --muted:#555;
  --grey-box:#e6e6e6;
  --white:#fff;
}
*{margin:0;padding:0;box-sizing:border-box}
html,body{width:1200px;height:2651px;overflow:hidden}
body{position:relative;background:var(--white);font-family:"Arimo",Arial,sans-serif;color:var(--text)}
.abs{position:absolute}

/* header */
.site-header{position:absolute;left:0;top:0;width:1200px;height:145px;background:var(--black)}
.brand{position:absolute;left:108px;top:28px;display:flex;align-items:center;gap:12px}
.brand-mark{width:34px;height:34px;border-radius:50%;background:var(--green)}
.brand-name{font-family:"PT Sans",sans-serif;font-size:30px;color:var(--green);letter-spacing:2px}
.call{position:absolute;right:98px;top:12px;font-family:"PT Sans",sans-serif;color:var(--white);font-size:22px;display:flex;align-items:center;gap:10px}
.call b{font-size:25px;font-weight:400}
.main-nav{position:absolute;right:98px;top:107px;display:flex;gap:0}
.main-nav a{font-family:"Arimo",sans-serif;font-size:14px;color:var(--white);text-decoration:none;margin-left:62px;position:relative;padding-bottom:14px}
.main-nav a.active::after{content:"";position:absolute;left:-3px;right:-3px;bottom:0;height:5px;background:var(--green)}

/* hero */
.hero{position:absolute;left:0;top:145px;width:1200px;height:514px;background:linear-gradient(120deg,#c9d87a 0%,#6f8f3a 35%,#4a5a2c 55%,#b9c86a 80%,#e8ecbf 100%)}
.hero-arrow{position:absolute;top:214px;width:96px;height:83px;background:rgba(90,90,90,.55)}
.hero-arrow.prev{left:0}
.hero-arrow.next{right:0;width:100px}

/* welcome */
.welcome-photo{left:102px;top:703px;width:312px;height:253px;border:4px solid #f0f0f0;box-shadow:0 0 4px rgba(0,0,0,.25);background:linear-gradient(160deg,#5d8a52,#2e3d44 60%,#7ea5c8)}
.welcome-title{left:443px;top:690px;font-family:"PT Sans",sans-serif;font-size:39px;font-weight:400;color:#444;letter-spacing:1px}
.welcome-title span{color:var(--green)}
.welcome-text{left:449px;top:740px;width:650px;font-size:13.6px;line-height:26px;color:var(--text)}
.btn-more{left:449px;top:919px;width:130px;height:42px;border:2px solid var(--green-deep);font-size:14px;font-weight:700;color:#333;display:flex;align-items:center;justify-content:center;letter-spacing:.5px}

/* services */
.services{position:absolute;left:0;top:1002px;width:1200px;height:548px;background:linear-gradient(180deg,#86dba4,#72d294)}
.section-title{position:absolute;left:0;width:1200px;text-align:center;font-family:"PT Sans",sans-serif;font-size:36px;color:#111;letter-spacing:1.5px}
.service-card{position:absolute;width:301px;height:170px;border:4px solid var(--white)}
.service-card .label{position:absolute;left:0;right:0;bottom:0;height:40px;background:rgba(0,0,0,.55);color:var(--white);font-family:"PT Sans",sans-serif;font-size:21px;padding-left:16px;line-height:40px}

/* disappear + news */
.disappear-title{left:106px;top:1584px;font-family:"PT Sans",sans-serif;font-size:31px;color:var(--green)}
.disappear-text{left:110px;top:1632px;width:585px;font-size:13.6px;line-height:26px}
.news{left:755px;top:1582px;width:345px;height:295px;background:var(--grey-box);padding:18px 24px}
.news h3{font-family:"PT Sans",sans-serif;font-weight:400;font-size:25px;color:var(--green);margin-bottom:10px}
.news p{font-size:13.6px;line-height:23px;color:#333}
.news strong{font-weight:700}

/* testimonials */
.testimonials{position:absolute;left:0;top:1928px;width:1200px;height:373px;background:linear-gradient(180deg,#7fd8a0,#6dcf90)}
.quote-badge{position:absolute;left:548px;top:92px;width:84px;height:84px;border-radius:50%;background:var(--white);display:flex;align-items:center;justify-content:center}
.quote-badge::before{content:"";position:absolute;inset:7px;border-radius:50%;background:var(--green-deep)}
.quote-badge svg{position:relative}
.testimonial-text{position:absolute;left:106px;top:196px;width:990px;text-align:center;font-family:"PT Sans",sans-serif;font-size:15.5px;line-height:26px;color:#1d1d1d}
.testimonial-name{position:absolute;left:0;width:1200px;text-align:center;font-family:"PT Sans",sans-serif;font-weight:700;font-size:14px;color:#111}

/* footer */
.site-footer{position:absolute;left:0;top:2301px;width:1200px;height:300px;background:var(--dark)}
.footer-title{position:absolute;left:0;top:28px;width:1200px;text-align:center;font-family:"Montserrat",sans-serif;font-weight:600;font-size:23px;color:var(--green);letter-spacing:.5px}
.footer-col{position:absolute;top:89px;list-style:none}
.footer-col li{font-size:14px;color:#eee;height:26px;display:flex;align-items:center;gap:10px}
.footer-col li svg{flex:none}
.copyright{position:absolute;left:0;top:2601px;width:1200px;height:50px;background:var(--green-band);color:var(--white);font-size:13px;display:flex;align-items:center;justify-content:center}
</style>
</head>
<body>

<header class="site-header">
  <div class="brand"><span class="brand-mark"></span><span class="brand-name">LEAFWELL</span></div>
  <div class="call">Call Now:
    <svg width="20" height="20" viewBox="0 0 24 24"><path fill="#5fcf8e" d="M6.6 10.8a15.1 15.1 0 0 0 6.6 6.6l2.2-2.2c.3-.3.7-.4 1-.2 1.1.4 2.3.6 3.6.6.6 0 1 .4 1 1V20c0 .6-.4 1-1 1C10.6 21 3 13.4 3 4c0-.6.4-1 1-1h3.5c.6 0 1 .4 1 1 0 1.3.2 2.5.6 3.6.1.3 0 .7-.2 1z"/></svg>
    <b>968-55510420</b></div>
  <nav class="main-nav">
    <a class="active">HOME</a><a>ABOUT</a><a>WHAT WE DO</a><a>COUPONS</a><a>THE BUZZ</a><a>CONTACT US</a>
  </nav>
</header>

<section class="hero" role="img" aria-label="Arborist in safety gear cutting a tree trunk with a chainsaw">
  <div class="hero-arrow prev"></div>
  <div class="hero-arrow next">
    <svg class="abs" style="left:46px;top:27px" width="18" height="30" viewBox="0 0 18 30"><path d="M3 3l12 12L3 27" stroke="#fff" stroke-width="4" fill="none"/></svg>
  </div>
</section>

<div class="abs welcome-photo" role="img" aria-label="Crew loading a wood chipper"></div>
<h1 class="abs welcome-title">WELCOME TO <span>LEAFWELL</span></h1>
<p class="abs welcome-text">Lorem ipsum dolor sit amet, consectetur adipiscing elit, sed do eiusmod tempor incididunt ut labore et dolore magna aliqua. Ut enim ad minim veniam, quis nostrud exercitation ullamco laboris nisi ut aliquip ex ea commodo consequat. Duis aute irure dolor in reprehenderit in voluptate velit esse cillum dolore eu fugiat nulla pariatur Sed ut perspiciatis unde omnis iste natus error sit voluptatem accusantium doloremque laudantium, totam rem aperiam, eaque ipsa quae ab illo inventore veritatis et quasi architecto beatae vitae dicta sunt explicabo..</p>
<div class="abs btn-more">LEARN MORE</div>

<section class="services">
  <h2 class="section-title" style="top:22px">OUR SERVICES</h2>
  <div class="service-card" style="left:102px;top:106px;background:linear-gradient(135deg,#6a7f8f,#4b3a2e 60%,#8a6a4a)" role="img" aria-label="Chainsaw cutting a trunk"><div class="label">Tree Removal</div></div>
  <div class="service-card" style="left:449px;top:106px;background:linear-gradient(160deg,#5b9be0,#3a6fb0 55%,#4a3a2e)" role="img" aria-label="Worker trimming branches against a blue sky"><div class="label">Tree Trimming</div></div>
  <div class="service-card" style="left:799px;top:106px;background:linear-gradient(160deg,#9bb46a,#6f8a3e 60%,#a07a4a)" role="img" aria-label="Stump grinder on a lawn"><div class="label">Stump Grinding</div></div>
  <div class="service-card" style="left:102px;top:325px;background:linear-gradient(180deg,#dfe8ef,#8a9a7a 50%,#4f7a3a)" role="img" aria-label="House with a large tree after a storm"><div class="label">Storm Damage</div></div>
  <div class="service-card" style="left:449px;top:325px;background:linear-gradient(160deg,#6a8fbf,#8a7a5a 50%,#4a3a2a)" role="img" aria-label="Climber installing tree cables"><div class="label">Tree Cabling</div></div>
  <div class="service-card" style="left:799px;top:325px;background:linear-gradient(180deg,#e6eef0,#a8b8a0 50%,#5d8a45)" role="img" aria-label="White bucket truck parked by trees"><div class="label">75' Bucket Truck</div></div>
</section>

<h2 class="abs disappear-title">We Make the Tree Disappear</h2>
<div class="abs disappear-text">
  <p>Lorem ipsum dolor sit amet, consectetur adipiscing elit, sed do eiusmod tempor incididunt ut labore et dolore magna aliqua. Ut enim ad minim veniam, quis nostrud exercitation ullamco laboris nisi ut aliquip ex ea commodo consequat. Duis aute irure dolor in reprehenderit in voluptate velit esse cillum dolore eu fugiat nulla pariatur Sed ut perspiciatis unde omnis iste natus error sit voluptatem.</p>
  <p style="margin-top:26px">Accusantium doloremque laudantium, totam rem aperiam, eaque ipsa quae ab illo inventore veritatis et quasi architecto beatae vitae dicta sunt explicabo..</p>
</div>
<aside class="abs news">
  <h3>News and Announcements</h3>
  <p><strong>Emerald Ash Bore (EAB) Special Notice</strong></p>
  <p>Do you have an Ash tree on your property? If so, you should be aware that they are now currently in our area.</p>
  <p>If your tree shows signs of low leaf count, heavy seed production or excessive "woodpecker" holes, you may have the EAB. The EAB will kill your tree within 3 years of infestation.</p>
  <p style="margin-top:4px"><strong>Call us to discuss your Ash trees.</strong></p>
</aside>

<section class="testimonials">
  <h2 class="section-title" style="top:22px">TESTIMONIALS</h2>
  <div class="quote-badge">
    <svg width="32" height="26" viewBox="0 0 32 26"><path fill="#fff" d="M0 0h13v13c0 7-4 12-11 13l-1-4c4-1 6-4 6-8H0zM19 0h13v13c0 7-4 12-11 13l-1-4c4-1 6-4 6-8h-7z"/></svg>
  </div>
  <p class="testimonial-text">A wonderful serenity has taken possession of my entire soul, like these sweet mornings of spring which I enjoy with my whole heartle heart. I am alone, and feel the charm of existence in this spot, which was created for the I am alone, and feel the charm of existence in this spot, which was created for the bliss of souls like mine. I am so happy.</p>
  <div class="testimonial-name" style="top:295px">JOHN DOE</div>
  <div class="testimonial-name" style="top:320px">YOGA, 8 months</div>
</section>

<footer class="site-footer">
  <h2 class="footer-title">COMPREHENSIVE SERVICES OFFERED BY LEAFWELL</h2>
  <ul class="footer-col" style="left:127px">
    <li><svg width="10" height="10" viewBox="0 0 10 10"><path d="M0 5h8M5 2l3 3-3 3" stroke="#fff" stroke-width="1.6" fill="none"/></svg>Certified Arborist</li>
    <li><svg width="10" height="10" viewBox="0 0 10 10"><path d="M0 5h8M5 2l3 3-3 3" stroke="#fff" stroke-width="1.6" fill="none"/></svg>Bucket  Service</li>
    <li><svg width="10" height="10" viewBox="0 0 10 10"><path d="M0 5h8M5 2l3 3-3 3" stroke="#fff" stroke-width="1.6" fill="none"/></svg>Crane Service</li>
    <li><svg width="10" height="10" viewBox="0 0 10 10"><path d="M0 5h8M5 2l3 3-3 3" stroke="#fff" stroke-width="1.6" fill="none"/></svg>Deadwooding</li>
    <li><svg width="10" height="10" viewBox="0 0 10 10"><path d="M0 5h8M5 2l3 3-3 3" stroke="#fff" stroke-width="1.6" fill="none"/></svg>Xl Tree Removal</li>
    <li><svg width="10" height="10" viewBox="0 0 10 10"><path d="M0 5h8M5 2l3 3-3 3" stroke="#fff" stroke-width="1.6" fill="none"/></svg>Ash Borer Control</li>
    <li><svg width="10" height="10" viewBox="0 0 10 10"><path d="M0 5h8M5 2l3 3-3 3" stroke="#fff" stroke-width="1.6" fill="none"/></svg>Pruning</li>
  </ul>
  <ul class="footer-col" style="left:364px">
    <li><svg width="10" height="10" viewBox="0 0 10 10"><path d="M0 5h8M5 2l3 3-3 3" stroke="#fff" stroke-width="1.6" fill="none"/></svg>Stump Grinding</li>
    <li><svg width="10" height="10" viewBox="0 0 10 10"><path d="M0 5h8M5 2l3 3-3 3" stroke="#fff" stroke-width="1.6" fill="none"/></svg>Root Collar Excavation</li>
    <li><svg width="10" height="10" viewBox="0 0 10 10"><path d="M0 5h8M5 2l3 3-3 3" stroke="#fff" stroke-width="1.6" fill="none"/></svg>Licensed Pest Control</li>
    <li><svg width="10" height="10" viewBox="0 0 10 10"><path d="M0 5h8M5 2l3 3-3 3" stroke="#fff" stroke-width="1.6" fill="none"/></svg>Vertical Mulching</li>
    <li><svg width="10" height="10" viewBox="0 0 10 10"><path d="M0 5h8M5 2l3 3-3 3" stroke="#fff" stroke-width="1.6" fill="none"/></svg>Tree Inventories</li>
    <li><svg width="10" height="10" viewBox="0 0 10 10"><path d="M0 5h8M5 2l3 3-3 3" stroke="#fff" stroke-width="1.6" fill="none"/></svg>Chipping Service</li>
    <li><svg width="10" height="10" viewBox="0 0 10 10"><path d="M0 5h8M5 2l3 3-3 3" stroke="#fff" stroke-width="1.6" fill="none"/></svg>Tree Selection Service</li>
  </ul>
  <ul class="footer-col" style="left:636px">
    <li><svg width="10" height="10" viewBox="0 0 10 10"><path d="M0 5h8M5 2l3 3-3 3" stroke="#fff" stroke-width="1.6" fill="none"/></svg>Tree/shrub Fertilization</li>
    <li><svg width="10" height="10" viewBox="0 0 10 10"><path d="M0 5h8M5 2l3 3-3 3" stroke="#fff" stroke-width="1.6" fill="none"/></svg>Spraying</li>
    <li><svg width="10" height="10" viewBox="0 0 10 10"><path d="M0 5h8M5 2l3 3-3 3" stroke="#fff" stroke-width="1.6" fill="none"/></svg>Lightning Protection</li>
    <li><svg width="10" height="10" viewBox="0 0 10 10"><path d="M0 5h8M5 2l3 3-3 3" stroke="#fff" stroke-width="1.6" fill="none"/></svg>Cable Bracing</li>
    <li><svg width="10" height="10" viewBox="0 0 10 10"><path d="M0 5h8M5 2l3 3-3 3" stroke="#fff" stroke-width="1.6" fill="none"/></svg>Disease Control</li>
    <li><svg width="10" height="10" viewBox="0 0 10 10"><path d="M0 5h8M5 2l3 3-3 3" stroke="#fff" stroke-width="1.6" fill="none"/></svg>Expert Climbers</li>
    <li><svg width="10" height="10" viewBox="0 0 10 10"><path d="M0 5h8M5 2l3 3-3 3" stroke="#fff" stroke-width="1.6" fill="none"/></svg>Disease Control</li>
  </ul>
  <ul class="footer-col" style="left:896px">
    <li><svg width="10" height="10" viewBox="0 0 10 10"><path d="M0 5h8M5 2l3 3-3 3" stroke="#fff" stroke-width="1.6" fill="none"/></svg>Commercial Service</li>
    <li><svg width="10" height="10" viewBox="0 0 10 10"><path d="M0 5h8M5 2l3 3-3 3" stroke="#fff" stroke-width="1.6" fill="none"/></svg>Tree Shaping</li>
    <li><svg width="10" height="10" viewBox="0 0 10 10"><path d="M0 5h8M5 2l3 3-3 3" stroke="#fff" stroke-width="1.6" fill="none"/></svg>Crown Reduction</li>
    <li><svg width="10" height="10" viewBox="0 0 10 10"><path d="M0 5h8M5 2l3 3-3 3" stroke="#fff" stroke-width="1.6" fill="none"/></svg>Planting</li>
    <li><svg width="10" height="10" viewBox="0 0 10 10"><path d="M0 5h8M5 2l3 3-3 3" stroke="#fff" stroke-width="1.6" fill="none"/></svg>Pre-construction</li>
    <li><svg width="10" height="10" viewBox="0 0 10 10"><path d="M0 5h8M5 2l3 3-3 3" stroke="#fff" stroke-width="1.6" fill="none"/></svg>Tree Preservation</li>
    <li><svg width="10" height="10" viewBox="0 0 10 10"><path d="M0 5h8M5 2l3 3-3 3" stroke="#fff" stroke-width="1.6" fill="none"/></svg>Consulting</li>
  </ul>
</footer>
<div class="copyright">Copyright 2010 © Leafwell Arbor Co. All Right Reserved.</div>

</body>
</html>
```